Copper lark buildworks

Copper lark buildworks is a small construction company.
Who is a licenced builder, Carpenter, joiner,
working on heritage ,new build, speacial projects and sometimes furniture

Industry/Entity Type

Construction

```html
<!DOCTYPE html>
<html lang="en">
<head>
<meta charset="utf-8">
<title>Copper lark buildworks – Business Card</title>
<link rel="stylesheet" href="https://fonts.googleapis.com/css2?family=Open+Sans:wght@400;600&display=swap">
<style>
  :root {
    --backdrop: #e7e5e0;
    --card-white: #f7f7f5;
    --lime-light: #b8e05c;
    --lime-deep: #84c23c;
    --ink: #1b1b1b;
    --band-black: #141414;
    --icon-line: #ffffff;
  }
  html, body {
    margin: 0;
    width: 1200px;
    height: 780px;
    overflow: hidden;
    background: var(--backdrop);
  }
  .canvas {
    position: relative;
    width: 1200px;
    height: 780px;
  }
  .business-card {
    position: absolute;
    left: 75px;
    top: 90px;
    width: 1050px;
    height: 600px;
    background: var(--card-white);
    box-shadow: 0 10px 30px rgba(0,0,0,0.18);
    overflow: hidden;
    font-family: "Open Sans", Arial, sans-serif;
  }
  .card-shapes {
    position: absolute;
    inset: 0;
  }
  .brand-block {
    position: absolute;
    left: 90px;
    top: 250px;
    display: flex;
    align-items: center;
    gap: 18px;
  }
  .brand-dot {
    width: 46px;
    height: 46px;
    border-radius: 50%;
    background: var(--lime-deep);
    flex: none;
  }
  .brand-name {
    font-size: 38px;
    font-weight: 600;
    color: var(--ink);
    line-height: 1.1;
    margin: 0;
    width: 300px;
  }
  .contact-block {
    position: absolute;
    right: 60px;
    top: 70px;
    text-align: right;
    color: var(--ink);
  }
  .person-name {
    font-size: 30px;
    font-weight: 400;
    margin: 0;
  }
  .person-title {
    font-size: 21px;
    margin: 2px 0 56px;
  }
  .contact-list {
    list-style: none;
    margin: 0;
    padding: 0;
  }
  .contact-item {
    display: flex;
    justify-content: flex-end;
    align-items: center;
    gap: 16px;
    font-size: 22px;
    margin-bottom: 18px;
  }
  .contact-icon {
    width: 30px;
    height: 30px;
    flex: none;
  }
</style>
</head>
<body>
<div class="canvas">
  <section class="business-card">
    <svg class="card-shapes" viewBox="0 0 1050 600" width="1050" height="600" aria-hidden="true">
      <defs>
        <linearGradient id="limeFill" x1="0" y1="0" x2="1" y2="1">
          <stop offset="0" stop-color="var(--lime-light)"/>
          <stop offset="1" stop-color="var(--lime-deep)"/>
        </linearGradient>
      </defs>
      <path class="black-band" d="M535,0 C585,210 515,440 360,600 L440,600 C580,430 618,210 570,0 Z" fill="var(--band-black)"/>
      <path class="white-gap" d="M560,0 C608,210 568,430 432,600 L446,600 C584,430 620,210 574,0 Z" fill="#ffffff"/>
      <path class="lime-panel" d="M572,0 C620,210 582,430 446,600 L1050,600 L1050,0 Z" fill="url(#limeFill)"/>
    </svg>

    <div class="brand-block">
      <span class="brand-dot"></span>
      <h1 class="brand-name">Copper lark buildworks</h1>
    </div>

    <div class="contact-block">
      <p class="person-name">Mara Ellison</p>
      <p class="person-title">President</p>
      <ul class="contact-list">
        <li class="contact-item">0400123987
          <svg class="contact-icon" viewBox="0 0 30 30"><circle cx="15" cy="15" r="13" fill="none" stroke="var(--icon-line)" stroke-width="2"/><path d="M10 9 l3 0 l1.5 3.5 l-2 1.5 a8 8 0 0 0 3.5 3.5 l1.5 -2 l3.5 1.5 l0 3 a2 2 0 0 1 -2 1.5 a12 12 0 0 1 -11 -11 a2 2 0 0 1 2 -1.5 z" fill="var(--icon-line)"/></svg>
        </li>
        <li class="contact-item">hello@copperlark.com
          <svg class="contact-icon" viewBox="0 0 30 30"><circle cx="15" cy="15" r="13" fill="none" stroke="var(--icon-line)" stroke-width="2"/><rect x="8" y="10" width="14" height="10" fill="none" stroke="var(--icon-line)" stroke-width="1.6"/><path d="M8 10 L15 16 L22 10" fill="none" stroke="var(--icon-line)" stroke-width="1.6"/></svg>
        </li>
        <li class="contact-item">www.copperlark.com
          <svg class="contact-icon" viewBox="0 0 30 30"><circle cx="15" cy="15" r="13" fill="none" stroke="var(--icon-line)" stroke-width="2"/><circle cx="15" cy="15" r="7.5" fill="none" stroke="var(--icon-line)" stroke-width="1.4"/><ellipse cx="15" cy="15" rx="3.2" ry="7.5" fill="none" stroke="var(--icon-line)" stroke-width="1.4"/><path d="M7.5 15 H22.5" stroke="var(--icon-line)" stroke-width="1.4"/></svg>
        </li>
      </ul>
    </div>
  </section>
</div>
</body>
</html>
```